Lidia Vanta Catering
Complete Stationery Design
Lidia Vanta Catering - Chef / Catering
Creative Brief
Bright & Fun-filled
Corazon Belmiro
Director, Sales & Marketing
2nd Floor, Quintero Bldg., Saldivar Avenue near corner Lupine Street, Navotas, Metro Manila, Philippines 1490
cbelmiro@lidiavanta-example.ph
www.lidiavanta-example.ph
Lidia Vanta is a high end catering company. Our design is modern Victorian. Color dark red, black and white but we are open to other color suggestion. We need the ff: - business cards - A4 and letter size paper with matching letter envelopes - Folder that fits A4 and letter size envelop - Fax Cover - CD sticker and cover - Sticker label - Address Sticker Label - Paper Bag Design - Styro lunch box design - Tissue Napkin Design - Name Plate - Identification Card Design
Victorian design with our Logo in the middle

```html
<!DOCTYPE html>
<html lang="en">
<head>
<meta charset="utf-8">
<title>Lidia Vanta Catering – Stationery Set</title>
<link href="https://fonts.googleapis.com/css2?family=Cormorant+Garamond:ital,wght@0,500;1,500&family=Lato:wght@400&display=swap" rel="stylesheet">
<style>
  :root{
    --backdrop:#2f2f31;
    --paper:#ffffff;
    --red:#b3121c;
    --red-dark:#7d0c13;
    --ink:#2a2a2a;
    --grey:#6d6d70;
    --grey-light:#a9a9ac;
    --black-card:#1b1b1c;
    --label:#8c8c8f;
    --watermark:rgba(120,120,120,.13);
  }
  *{box-sizing:border-box;margin:0;padding:0}
  html,body{width:1200px;height:312px;overflow:hidden;background:var(--backdrop)}
  body{position:relative;font-family:"Lato",sans-serif;color:var(--ink)}
  .item{position:absolute;background:var(--paper);overflow:hidden;box-shadow:0 2px 6px rgba(0,0,0,.45)}
  .item svg.band{position:absolute;inset:0;width:100%;height:100%}
  .brand{font-family:"Cormorant Garamond",serif;font-style:italic;font-weight:500;color:var(--ink);white-space:nowrap;text-align:center;position:absolute;left:0;right:0}
  .watermark{font-family:"Cormorant Garamond",serif;font-style:italic;font-weight:500;color:var(--watermark);position:absolute;left:0;right:0;text-align:center;white-space:nowrap}
  .fine{font-size:3.4px;line-height:1.35;color:var(--grey);position:absolute;text-align:center;left:0;right:0}
  .label{position:absolute;font-size:5px;color:var(--label);letter-spacing:.3px;white-space:nowrap}

  /* business cards */
  .card{width:70px;height:38px}
  .card--dark{background:var(--black-card)}
  .card--dark .brand{color:#e9e9e9}
  .card .brand{font-size:9px;top:11px}
  .card .fine{top:24px}

  /* letterheads */
  .letterhead{top:19px;width:197px;height:281px}
  .letterhead .brand{font-size:12px;top:14px}
  .letterhead .watermark{font-size:34px;top:120px}
  .letterhead .fine{bottom:10px}

  /* envelopes */
  .envelope{left:643px;width:221px}
  .envelope .brand{font-size:10px;left:18px;right:auto;top:12px}
  .envelope .watermark{font-size:26px;top:34px}

  /* envelope stack */
  .stack{left:888px;width:300px;height:76px}
  .stack--red{top:19px;background:var(--red);z-index:4}
  .stack--grey{top:90px;background:#8a8a8d;z-index:3}
  .stack--white{top:170px;z-index:2}
  .stack--white2{top:240px;height:48px;z-index:1}
  .stack .brand{font-size:10px;top:8px;color:#fff}
</style>
</head>
<body>

  <!-- Business cards -->
  <div class="item card" style="left:19px;top:113px">
    <svg class="band" viewBox="0 0 70 38" preserveAspectRatio="none"><path d="M0 30 Q30 34 70 26 L70 38 L0 38Z" fill="var(--red)"/></svg>
    <div class="brand">Lidia Vanta</div>
    <div class="fine">Catering</div>
  </div>
  <div class="item card card--dark" style="left:96px;top:113px">
    <div class="fine" style="top:9px;color:#ccc">Corazon Belmiro<br>Director, Sales &amp; Marketing<br>cbelmiro@lidiavanta-example.ph<br>www.lidiavanta-example.ph</div>
  </div>
  <div class="item card" style="left:19px;top:161px">
    <svg class="band" viewBox="0 0 70 38" preserveAspectRatio="none"><path d="M0 0 L14 0 Q6 18 0 30Z" fill="var(--red)"/></svg>
    <div class="fine" style="top:9px">Corazon Belmiro<br>Director, Sales &amp; Marketing<br>cbelmiro@lidiavanta-example.ph<br>www.lidiavanta-example.ph</div>
  </div>
  <div class="item card card--dark" style="left:96px;top:161px">
    <div class="brand">Lidia Vanta</div>
    <div class="fine" style="color:#aaa">Catering</div>
  </div>
  <div class="label" style="left:40px;top:204px">Business Cards</div>

  <!-- Letterhead A4 -->
  <div class="item letterhead" style="left:216px">
    <svg class="band" viewBox="0 0 197 281" preserveAspectRatio="none">
      <path d="M150 0 L197 0 L197 60 Q185 20 150 0Z" fill="var(--red)"/>
      <path d="M0 200 Q14 250 55 281 L0 281Z" fill="var(--red)"/>
    </svg>
    <div class="brand">Lidia Vanta</div>
    <div class="watermark">Lidia Vanta</div>
    <div class="fine">2nd Floor, Quintero Bldg., Saldivar Avenue near corner Lupine Street, Navotas, Metro Manila, Philippines 1490<br>cbelmiro@lidiavanta-example.ph · www.lidiavanta-example.ph</div>
  </div>
  <div class="label" style="left:290px;top:303px">Letterhead A4</div>

  <!-- Letterhead Letter -->
  <div class="item letterhead" style="left:432px">
    <svg class="band" viewBox="0 0 197 281" preserveAspectRatio="none">
      <path d="M0 0 L40 0 Q12 40 0 110Z" fill="var(--red)"/>
      <path d="M0 180 Q10 240 36 281 L0 281Z" fill="var(--red)"/>
    </svg>
    <div class="brand">Lidia Vanta</div>
    <div class="watermark">Lidia Vanta</div>
    <div class="fine">2nd Floor, Quintero Bldg., Saldivar Avenue near corner Lupine Street, Navotas, Metro Manila, Philippines 1490<br>cbelmiro@lidiavanta-example.ph · www.lidiavanta-example.ph</div>
  </div>
  <div class="label" style="left:500px;top:303px">Letterhead Letter</div>

  <!-- Envelopes front -->
  <div class="item envelope" style="top:43px;height:106px">
    <svg class="band" viewBox="0 0 221 106" preserveAspectRatio="none"><path d="M0 0 L34 0 Q8 30 0 70Z" fill="var(--red)"/></svg>
    <div class="brand">Lidia Vanta</div>
  </div>
  <div class="label" style="left:730px;top:152px">Envelope A4</div>

  <div class="item envelope" style="top:168px;height:101px">
    <svg class="band" viewBox="0 0 221 101" preserveAspectRatio="none"><path d="M0 60 Q10 88 40 101 L0 101Z" fill="var(--red)"/></svg>
    <div class="brand">Lidia Vanta</div>
  </div>
  <div class="label" style="left:726px;top:272px">Envelope Letter</div>

  <!-- Envelope backs -->
  <div class="item stack stack--red">
    <svg class="band" viewBox="0 0 300 76" preserveAspectRatio="none"><path d="M0 0 L150 34 L300 0" fill="none" stroke="var(--red-dark)" stroke-width="1"/></svg>
    <div class="brand">Lidia Vanta</div>
  </div>
  <div class="item stack stack--grey">
    <svg class="band" viewBox="0 0 300 76" preserveAspectRatio="none"><path d="M0 0 L150 34 L300 0" fill="none" stroke="#6f6f72" stroke-width="1"/></svg>
  </div>
  <div class="item stack stack--white">
    <svg class="band" viewBox="0 0 300 76" preserveAspectRatio="none"><path d="M0 0 L150 34 L300 0" fill="none" stroke="#d4d4d6" stroke-width="1"/></svg>
  </div>
  <div class="item stack stack--white2">
    <svg class="band" viewBox="0 0 300 48" preserveAspectRatio="none"><path d="M0 0 L150 22 L300 0" fill="none" stroke="#d4d4d6" stroke-width="1"/></svg>
  </div>
  <div class="label" style="left:1010px;top:293px">Envelope Backs</div>

</body>
</html>
```